Modern Website Design for an Online Travel Agency.. Design Only!!

Hi there!

We are building an website for our travel agency that caters to tourists traveling to the Cayman Islands. We provide travel information and take bookings for various tours available here.

We need designs for 8 different web page layouts. You can see the layout specifications in two attached documents. We do not have a need for the coding to be done. This will simply act as a blueprint for our developer to build from.

The important pages are the 'Home Page' 'checkout page' and the ‘Checkout Page’ (Page 1 & 10 in the PDF ‘Website Layout’)

The MOST important page is ‘Tour Search Page’ (page 6)

If you intend on only submitting one page design, please submit a design for page 6. Be aware though, the more of these 3 page designs you submit, the more likely we are to move forward with you!

At this stage, we are simply looking to develop the most aesthetic website design layout possible.

- The website should be colour coordinated with the logo. You can most certainly use other colours if you feel they complement the overall design of the website well.

- Everything must be laid out in an EXTREMELY simple & ‘easy to navigate’ way. The key is simplicity & Functionality. There is no need for messy or elaborate graphics.

- The website MUST have a VERY clean and modern appearance.

- We want the main background to be white, but you can use light grey in places to compliment or add dimension if you feel necessary.

- We will appreciate a good use of shadows and especially a good use of icons. (You can see examples of icons we have already designed, we are definitely open to new icon design concepts too)

- We will reward imagination and original thinking! Essentially we want a website with a creative touch and unique design elements, whilst maintaining that clean and simple layout.

- Most importantly!! - Paying attention to the small details will be highly rewarded (A well balanced and seamless use of fonts, colours, dimensions, shadowing, positioning, etc)

If you have any questions, please don’t hesitate to ask.

We’re excited to see your design submissions!

Thank you!!

You can find all the support documents and content at: https://www.filevorra.net/sh/9qm2rtwplexan7c/QQBmTtZnPdLsWEGxvvaJpLmRw?dl=0

Target Market(s)

Tourists

Industry/Entity Type

Travel

Number of Pages Required

5+ page

Font styles to use
Sans Serif

Colors

Designer to choose colors to be used in the design.

Requirements
Must have
• Must be very clean and modern.
• Must be simple and bold
• Must be color coordinated in a way that makes sense
• White background
Nice to have
• Good use of shadows and Icons
Should not have
• Over use of messy graphics
• And design layout which is not right angled (using anything but vertical or horizontal for the edges in the design)

```html
<!DOCTYPE html>
<html lang="en">
<head>
<meta charset="utf-8">
<title>IsleWays – Home</title>
<link href="https://fonts.googleapis.com/css2?family=Roboto:wght@400;500;700;900&display=swap" rel="stylesheet">
<style>
  :root {
    --blue: #0a5ad4;
    --blue-dark: #0049b8;
    --green: #8dc63f;
    --navy: #1d3557;
    --topbar: #e4edf8;
    --grey-band: #efefef;
    --text: #2b2b2b;
    --muted: #777;
    --white: #ffffff;
  }
  * { margin: 0; padding: 0; box-sizing: border-box; }
  html, body { width: 1200px; height: 1200px; overflow: hidden; background: var(--white); }
  body { position: relative; font-family: 'Roboto', sans-serif; color: var(--text); }
  .page { position: absolute; left: 65px; top: 0; width: 1068px; height: 1200px; background: var(--white); }

  .topbar { position: absolute; left: 0; top: 0; width: 100%; height: 36px; background: var(--topbar); }
  .social { position: absolute; left: 659px; top: 11px; display: flex; gap: 12px; }
  .social span { width: 13px; height: 13px; border-radius: 50%; background: #8a8f96; display: block; }
  .select-mini { position: absolute; top: 7px; height: 22px; background: #f3f6fa; font-size: 10px; color: #444;
    display: flex; align-items: center; justify-content: space-between; padding: 0 7px 0 9px; }
  .select-mini::after { content: ""; border-left: 4px solid transparent; border-right: 4px solid transparent; border-top: 6px solid #333; }
  .lang { left: 790px; width: 54px; }
  .currency { left: 856px; width: 57px; }
  .login { position: absolute; left: 928px; top: 7px; width: 58px; height: 23px; background: var(--green); color: var(--white);
    font-size: 10px; font-weight: 700; display: flex; align-items: center; justify-content: center; }
  .search-icon { position: absolute; left: 1000px; top: 6px; }

  .header { position: absolute; left: 0; top: 36px; width: 100%; height: 54px; }
  .brand { position: absolute; left: 43px; top: 10px; display: flex; align-items: center; gap: 10px; }
  .brand-mark { width: 34px; height: 34px; background: var(--green); }
  .brand-name { font-size: 34px; font-weight: 700; color: var(--blue); letter-spacing: 0.5px; }
  .destinations { position: absolute; left: 885px; top: 14px; width: 141px; height: 28px; border: 1px solid #9a9a9a;
    font-size: 12px; color: #888; display: flex; align-items: center; justify-content: space-between; padding: 0 9px; }
  .destinations::after { content: ""; border-left: 4px solid transparent; border-right: 4px solid transparent; border-top: 6px solid #333; }

  .nav { position: absolute; left: 0; top: 90px; width: 100%; height: 42px; background: var(--blue);
    border-bottom: 1px solid var(--green); }
  .nav a { position: absolute; top: 14px; transform: translateX(-50%); color: var(--white); font-size: 12px;
    font-weight: 700; text-decoration: none; white-space: nowrap; }

  .hero { position: absolute; left: 0; top: 132px; width: 100%; height: 580px;
    background: linear-gradient(180deg, #3d6b9c 0%, #6d93bb 30%, #2f6f9a 52%, #1e5b85 72%, #2d5573 100%); overflow: hidden; }
  .hero-title { position: absolute; left: 0; top: 124px; width: 100%; text-align: center; color: var(--white);
    font-size: 47px; font-weight: 900; text-shadow: 0 2px 6px rgba(0,0,0,.45); }
  .hero-sub { position: absolute; left: 0; top: 205px; width: 100%; text-align: center; color: var(--white);
    font-size: 29px; font-weight: 400; text-shadow: 0 2px 6px rgba(0,0,0,.45); }
  .arrow { position: absolute; top: 226px; width: 33px; height: 33px; border-radius: 50%; background: var(--green);
    display: flex; align-items: center; justify-content: center; }
  .arrow.prev { left: 30px; }
  .arrow.next { left: 1007px; }
  .hero-curve { position: absolute; left: 0; top: 0; }

  .intro { position: absolute; left: 0; top: 650px; width: 100%; text-align: center; }
  .section-title { font-size: 29px; font-weight: 700; }
  .section-title .b { color: var(--blue); }
  .section-title .g { color: var(--green); }
  .body-text { width: 870px; margin: 0 auto; font-size: 14.5px; line-height: 20px; color: var(--text); }
  .intro .section-title { margin-bottom: 14px; }
  .intro .body-text + .body-text { margin-top: 20px; }
  .btn { display: inline-flex; align-items: center; justify-content: center; width: 123px; height: 32px;
    font-size: 15px; font-weight: 500; }
  .btn-blue { background: var(--blue); color: var(--white); margin-top: 27px; }

  .welcome { position: absolute; left: 0; top: 933px; width: 100%; height: 250px; background: var(--grey-band); text-align: center; padding-top: 27px; }
  .welcome .section-title { color: #222; margin-bottom: 16px; }
  .btn-green { background: var(--green); color: var(--blue); margin-top: 29px; }
</style>
</head>
<body>
<div class="page">
  <div class="topbar">
    <div class="social" aria-label="Social links"><span></span><span></span><span></span><span></span></div>
    <div class="select-mini lang">EN</div>
    <div class="select-mini currency">USD$</div>
    <div class="login">LOGIN</div>
    <svg class="search-icon" width="24" height="24" viewBox="0 0 24 24" aria-label="Search">
      <circle cx="10" cy="10" r="7.5" fill="none" stroke="#0a5ad4" stroke-width="2.4"/>
      <line x1="15.5" y1="15.5" x2="22" y2="22" stroke="#0a5ad4" stroke-width="2.8" stroke-linecap="round"/>
    </svg>
  </div>

  <header class="header">
    <div class="brand"><span class="brand-mark"></span><span class="brand-name">IsleWays</span></div>
    <div class="destinations">Destinations</div>
  </header>

  <nav class="nav">
    <a href="#" style="left:324px">DISCOVER CAYMAN</a>
    <a href="#" style="left:451px">THING TO DO</a>
    <a href="#" style="left:575px">MY TRIP PLAN</a>
    <a href="#" style="left:673px">MAP</a>
    <a href="#" style="left:763px">CONTACT US</a>
  </nav>

  <section class="hero">
    <div role="img" aria-label="Family and friends jumping joyfully on a beach at sunset with the sea behind" style="position:absolute;inset:0;"></div>
    <h1 class="hero-title">CAYMAN ISLANDS</h1>
    <p class="hero-sub">CAYMAN ISLANDS, BERMUDA, BAHAMAS, ETC</p>
    <div class="arrow prev"><svg width="12" height="12" viewBox="0 0 12 12"><polyline points="8,1 3,6 8,11" fill="none" stroke="#fff" stroke-width="1.6"/></svg></div>
    <div class="arrow next"><svg width="12" height="12" viewBox="0 0 12 12"><polyline points="4,1 9,6 4,11" fill="none" stroke="#fff" stroke-width="1.6"/></svg></div>
    <svg class="hero-curve" width="1068" height="580" viewBox="0 0 1068 580">
      <path d="M0,555 C180,440 360,432 500,434 C720,437 900,492 1068,574 L1068,580 L0,580 Z" fill="#1d3557"/>
      <path d="M0,548 C180,432 360,424 500,426 C720,429 900,484 1068,566 L1068,572 C900,492 720,440 500,438 C360,437 180,446 0,563 Z" fill="#8dc63f"/>
      <path d="M0,572 C190,455 360,442 500,444 C720,447 900,498 1068,580 L0,580 Z" fill="#ffffff"/>
    </svg>
  </section>

  <section class="intro">
    <h2 class="section-title"><span class="b">Company</span> <span class="g">Introduction</span></h2>
    <p class="body-text">In 2004 Mark Delaney, an avid horseman, and his wife Irene, founded the company Windward Trails. Its true beginnings however were born decades earlier in Mark’s mind. His passion for horses began a child, when he learned how to care for the magnificent, graceful creatures.</p>
    <p class="body-text">The company name Windward Trails was chosen for the fact that horses have a spirit that is by most accounts, unbreakable, just as Mark and Irene being devoted Christians, have unbreakable faith. Windward Trails was established to offer trail rides on some of the world’s most beautiful beaches, in Grand Cayman.</p>
    <a class="btn btn-blue">Show More</a>
  </section>

  <section class="welcome">
    <h2 class="section-title">Welcome to <span class="b">Isle</span><span class="g">Ways</span></h2>
    <p class="body-text">We are proud travel concierges of the Cayman Islands! We help thousands of tourists visiting Cayman every year arrange vacation getaway catered to their exact needs. With a wealth of local knowledge, we help you avoid unreliable tour operators and find those local hidden gems. Here you can research everything you need to be fully prepared for your travelsandalso view the complete range of activities available.</p>
    <a class="btn btn-green">Show More</a>
  </section>
</div>
</body>
</html>
```